Website design for company that sells taximeters and has a taxi dispatch call center, webstore neede

Need a website with a shop with at least 20 articles, in two languages, possibly by using a purchased theme (not purchased yet).The company provides equipments and dispatch solutions for taxi companies. Typical yellow and black theme

Target Market(s)

Taxi companies

Industry/Entity Type

Taxi

Number of Pages Required

3 page

Font styles to use
Sans Serif

Colors
fbed22
000000

Requirements
Must have
• - webstore for at least 20 articles
• - Documents folder where to put pdf material related to taximeters
• - contact form message submission
Nice to have
• Feedback section
Should not have
• Blogs,

```html
<!DOCTYPE html>
<html lang="en">
<head>
<meta charset="utf-8">
<title>Farelane – Shop</title>
<link href="https://fonts.googleapis.com/css2?family=Montserrat:wght@400;500;600;700;800&family=Open+Sans:wght@400;600;700&display=swap" rel="stylesheet">
<style>
:root{
  --yellow:#f5c518;
  --yellow-bright:#fbed22;
  --black:#0c0c0c;
  --ink:#1b1b1b;
  --grey:#9a9a9a;
  --grey-light:#c9c9c9;
  --line:#dcdcdc;
  --panel:#efefef;
  --navy:#1f2a36;
  --accent-red:#e5533d;
  --white:#fff;
}
*{margin:0;padding:0;box-sizing:border-box}
html,body{width:707px;height:1200px;overflow:hidden;background:var(--white)}
body{position:relative;font-family:"Open Sans",sans-serif;color:var(--ink)}
.abs{position:absolute}

/* hero */
.hero{position:absolute;left:0;top:0;width:707px;height:169px;
  background:radial-gradient(ellipse at 20% 90%,#6a5210 0%,transparent 35%),
  radial-gradient(ellipse at 78% 75%,#5a4a12 0%,transparent 30%),
  linear-gradient(180deg,#1a1c20 0%,#26241e 60%,#14130f 100%)}
.brand{left:88px;top:10px;font-family:"Montserrat",sans-serif;font-weight:800;font-size:14px;letter-spacing:.5px;color:var(--yellow-bright)}
.nav{left:230px;top:13px;display:flex;gap:17px;font-family:"Montserrat",sans-serif;font-weight:700;font-size:6.5px;letter-spacing:3.2px;color:var(--white)}
.phone{left:446px;top:9px;display:flex;align-items:center;gap:6px;font-family:"Montserrat",sans-serif;font-weight:600;font-size:6.5px;letter-spacing:1.2px;color:var(--yellow-bright)}
.lang{left:524px;top:12px;font-family:"Montserrat",sans-serif;font-weight:700;font-size:6px;color:var(--white)}
.search{left:578px;top:8px;width:91px;height:17px;border:1.6px solid var(--yellow-bright);border-radius:9px;
  font-family:"Montserrat",sans-serif;font-size:6.5px;color:#cfcfcf;padding:3px 0 0 9px;letter-spacing:.5px}
.search svg{position:absolute;right:7px;top:3px}
.hero-title{left:0;width:707px;top:69px;text-align:center;font-family:"Montserrat",sans-serif;font-weight:700;font-size:17px;letter-spacing:1.6px;color:var(--white)}
.hero-sub{left:0;width:707px;top:95px;text-align:center;font-family:"Montserrat",sans-serif;font-weight:700;font-size:6px;letter-spacing:.8px;color:var(--white)}

/* promo */
.promo{left:143px;top:194px;width:428px;height:103px;background:var(--panel)}
.promo-title{left:20px;top:17px;font-family:"Montserrat",sans-serif;font-size:13.5px;color:var(--ink);letter-spacing:-.2px}
.promo-title b{font-weight:700}
.promo-sub{left:20px;top:36px;font-family:"Montserrat",sans-serif;font-size:11px;letter-spacing:1.3px;color:#333}
.promo-price{left:20px;top:55px;font-family:"Montserrat",sans-serif;font-size:4.5px;color:#444;display:flex;align-items:baseline;gap:3px}
.promo-price strong{font-size:12px;color:var(--yellow);letter-spacing:1px}
.btn-shop{left:19px;top:72px;width:58px;height:18px;border-radius:9px;background:var(--yellow);color:var(--white);
  font-family:"Montserrat",sans-serif;font-weight:700;font-size:6.5px;letter-spacing:.8px;text-align:center;line-height:18px}
.promo-visual{left:211px;top:20px;width:144px;height:62px;border-radius:14px;background:linear-gradient(180deg,#2a2a2a,#0d0d0d)}

/* sidebar */
.side{left:143px;width:102px}
.side-head{font-family:"Montserrat",sans-serif;font-weight:700;font-size:6.5px;letter-spacing:.4px;color:#333;position:relative;height:12px}
.side-head::after{content:"";position:absolute;left:0;bottom:-2px;width:38px;height:2px;background:var(--yellow)}
.side-head .toggle{position:absolute;right:0;top:-1px;width:8px;height:8px;border:1px solid #aaa;border-radius:50%}
.side-head .toggle::before,.side-head .toggle::after{content:"";position:absolute;background:#aaa}
.side-head .toggle::before{left:1.5px;top:2.8px;width:3px;height:.8px}
.side-head .toggle::after{left:2.6px;top:1.6px;width:.8px;height:3px}
.side-rule{border-bottom:1px solid var(--line)}
.cat{font-size:5.5px;color:#888;letter-spacing:.4px;border-bottom:1px solid var(--line);position:absolute;left:0;width:102px;padding-bottom:6px}
.price-row{left:0;top:35px;font-size:4.5px;color:#777}
.price-row span{color:var(--accent-red)}
.btn-filter{left:64px;top:28px;width:37px;height:14px;background:var(--navy);color:var(--white);font-family:"Montserrat",sans-serif;font-weight:700;font-size:5px;text-align:center;line-height:14px}
.brand-item{position:absolute;left:0;width:102px;height:17px;border-bottom:1px solid var(--line);font-size:4.5px;color:#888;display:flex;align-items:center;letter-spacing:.4px}
.brand-item i{width:7px;height:7px;border:1px solid #ccc;margin-right:4px}
.brand-item em{margin-left:auto;font-style:normal}

/* toolbar */
.toolbar{left:256px;top:335px;width:309px;height:14px;font-size:6px;color:#555}
.toolbar::after{content:"";position:absolute;left:0;bottom:-3px;width:57px;height:2px;background:var(--yellow)}
.sortby{position:absolute;left:104px;top:1px;font-size:5px;color:#aaa;display:flex;gap:7px}
.sortby b{font-weight:400;color:#666}
.view{position:absolute;top:-3px;width:13px;height:13px;border:1px solid #ccc}

/* grid */
.grid{left:258px;top:360px;display:grid;grid-template-columns:repeat(3,99px);grid-auto-rows:142px;column-gap:4px;row-gap:11px}
.card{position:relative;border:1px solid #e6e6e6;background:var(--white)}
.badge{position:absolute;left:6px;top:6px;width:19px;height:7px;border-radius:4px;background:var(--yellow);color:var(--white);font-size:3.2px;font-weight:700;text-align:center;line-height:7px}
.card-img{position:absolute;left:13px;top:30px;width:72px;height:46px;border-radius:4px}
.card-img.meter{background:linear-gradient(180deg,#9a9a9a,#3a3a3a);border-radius:5px}
.card-img.radio{left:20px;top:24px;width:60px;height:54px;background:radial-gradient(ellipse at 60% 55%,#2b2b2b 0%,#2b2b2b 40%,transparent 72%)}
.card-name{position:absolute;left:7px;top:99px;font-size:6.5px;line-height:7px;color:#aaa;width:80px}
.card-price{position:absolute;left:7px;top:119px;font-family:"Montserrat",sans-serif;font-size:8.5px;font-weight:500;color:var(--black)}
.card-add{position:absolute;right:5px;bottom:-6px;width:15px;height:15px;border:1.5px solid var(--yellow);border-radius:50%;background:var(--white)}
.card-add::before,.card-add::after{content:"";position:absolute;background:var(--yellow)}
.card-add::before{left:3px;top:5.5px;width:6px;height:1.4px}
.card-add::after{left:5.3px;top:3.2px;width:1.4px;height:6px}

/* pagination */
.pager-rule{left:256px;top:988px;width:309px;height:1.5px;background:#333}
.pager-info{left:256px;top:999px;font-size:4.8px;color:#aaa}
.pager{left:434px;top:996px;display:flex;gap:3px}
.pager span{height:20px;border:1px solid #ddd;font-family:"Montserrat",sans-serif;font-weight:600;font-size:5px;letter-spacing:.5px;line-height:18px;text-align:center;color:#333}

/* footer */
.footer{left:0;top:1060px;width:707px;height:140px;background:var(--black);color:var(--white)}
.f-col{position:absolute;top:25px;font-size:5px;line-height:8.5px}
.f-col h4{font-family:"Montserrat",sans-serif;font-weight:700;font-size:5.2px;margin-bottom:5px;letter-spacing:.2px}
.f-col h4 span,.f-col a{color:var(--yellow);text-decoration:none}
.socials{display:flex;gap:3px}
.socials i{width:7px;height:7px;background:var(--white);border-radius:50%}
.f-rule{position:absolute;left:149px;top:84px;width:416px;height:1px;background:#555}
.f-copy{position:absolute;left:149px;top:91px;font-size:4.5px}
.f-copy span{color:var(--yellow)}
</style>
</head>
<body>

<header class="hero" role="img" aria-label="Night street scene with lit taxi roof signs">
</header>
<div class="abs brand">FARELANE</div>
<nav class="abs nav"><span>HOME</span><span>SHOP</span><span>CONTACT US</span></nav>
<div class="abs phone">
  <svg width="11" height="11" viewBox="0 0 24 24" fill="none" stroke="#fff" stroke-width="2"><path d="M5 3h4l2 5-3 2a11 11 0 0 0 6 6l2-3 5 2v4a2 2 0 0 1-2 2A17 17 0 0 1 3 5a2 2 0 0 1 2-2z"/></svg>
  555.014.2290
</div>
<div class="abs lang">ENG ˅</div>
<div class="abs search">search
  <svg width="9" height="9" viewBox="0 0 24 24" fill="none" stroke="#fff" stroke-width="2.4"><circle cx="10" cy="10" r="7"/><path d="M15 15l6 6"/></svg>
</div>
<h1 class="abs hero-title">WELCOME TO THE SHOP</h1>
<p class="abs hero-sub">EVERYTHING YOU'RELOOKING FOR IS RIGHT BELOW.</p>

<section class="abs promo">
  <div class="abs promo-title"><b>FLAT 50% DISCOUNT</b> ON</div>
  <div class="abs promo-sub">MIRROR METERS</div>
  <div class="abs promo-price">STARTING AT <strong>190.99$</strong></div>
  <div class="abs btn-shop">Shop Now</div>
  <div class="abs promo-visual" role="img" aria-label="Rear-view mirror taximeter with red digital display"></div>
</section>

<aside class="abs side" style="top:339px">
  <div class="side-head">CATEGORIES<span class="toggle"></span></div>
  <div class="cat" style="top:22px">Taximeters (8)</div>
  <div class="cat" style="top:45px">Dispatch Radios (10)</div>
  <div class="cat" style="top:69px">Taximeters (8)</div>
  <div class="cat" style="top:92px">Taximeters (8)</div>
  <div class="cat" style="top:114px">Dispatch Radios (10)</div>
  <div class="cat" style="top:138px">Taximeters (8)</div>
  <div class="cat" style="top:165px">Dispatch Radios (10)</div>
  <div class="cat" style="top:188px">Taximeters (8)</div>
</aside>

<aside class="abs side" style="top:555px">
  <div class="side-head">FILTER BY PRICE<span class="toggle"></span></div>
  <div class="abs price-row">Price: <span>$1100 to $1850</span></div>
  <div class="abs btn-filter">Filter</div>
</aside>

<aside class="abs side" style="top:616px">
  <div class="side-head">BRANDS<span class="toggle"></span></div>
  <div class="brand-item" style="top:16px"><i></i>Vantor<em>(7)</em></div>
  <div class="brand-item" style="top:33px"><i></i>Kelsen<em>(7)</em></div>
  <div class="brand-item" style="top:50px"><i></i>Vantor<em>(7)</em></div>
  <div class="brand-item" style="top:67px"><i></i>Kelsen<em>(7)</em></div>
  <div class="brand-item" style="top:84px"><i></i>Vantor<em>(7)</em></div>
  <div class="brand-item" style="top:101px"><i></i>Vantor<em>(7)</em></div>
  <div class="brand-item" style="top:118px"><i></i>Vantor<em>(7)</em></div>
</aside>

<div class="abs toolbar">Showing of 1-12 of 125 results
  <div class="sortby">Sort by <b>Price</b><b>Name</b><b>Date</b><b>Popular</b></div>
  <span class="view" style="left:274px;border-color:#ddd"></span>
  <span class="view" style="left:294px;border-color:#555"></span>
</div>

<main class="abs grid">
  <div class="card"><span class="badge">NEW</span><div class="card-img meter" role="img" aria-label="Taximeter with red display"></div><p class="card-name">Placeholder product Style</p><p class="card-price">303.50$</p><span class="card-add"></span></div>
  <div class="card"><span class="badge">NEW</span><div class="card-img radio" role="img" aria-label="Dispatch radio with coiled microphone"></div><p class="card-name">Placeholder product Style</p><p class="card-price">303.50$</p><span class="card-add"></span></div>
  <div class="card"><span class="badge">NEW</span><div class="card-img meter" role="img" aria-label="Taximeter with red display"></div><p class="card-name">Placeholder product Style</p><p class="card-price">303.50$</p><span class="card-add"></span></div>
  <div class="card"><span class="badge">NEW</span><div class="card-img meter" role="img" aria-label="Taximeter with red display"></div><p class="card-name">Placeholder product Style</p><p class="card-price">303.50$</p><span class="card-add"></span></div>
  <div class="card"><span class="badge">NEW</span><div class="card-img radio" role="img" aria-label="Dispatch radio with coiled microphone"></div><p class="card-name">Placeholder product Style</p><p class="card-price">303.50$</p><span class="card-add"></span></div>
  <div class="card"><span class="badge">NEW</span><div class="card-img meter" role="img" aria-label="Taximeter with red display"></div><p class="card-name">Placeholder product Style</p><p class="card-price">303.50$</p><span class="card-add"></span></div>
  <div class="card"><span class="badge">NEW</span><div class="card-img meter" role="img" aria-label="Taximeter with red display"></div><p class="card-name">Placeholder product Style</p><p class="card-price">303.50$</p><span class="card-add"></span></div>
  <div class="card"><span class="badge">NEW</span><div class="card-img radio" role="img" aria-label="Dispatch radio with coiled microphone"></div><p class="card-name">Placeholder product Style</p><p class="card-price">303.50$</p><span class="card-add"></span></div>
  <div class="card"><span class="badge">NEW</span><div class="card-img meter" role="img" aria-label="Taximeter with red display"></div><p class="card-name">Placeholder product Style</p><p class="card-price">303.50$</p><span class="card-add"></span></div>
  <div class="card"><span class="badge">NEW</span><div class="card-img meter" role="img" aria-label="Taximeter with red display"></div><p class="card-name">Placeholder product Style</p><p class="card-price">303.50$</p><span class="card-add"></span></div>
  <div class="card"><span class="badge">NEW</span><div class="card-img radio" role="img" aria-label="Dispatch radio with coiled microphone"></div><p class="card-name">Placeholder product Style</p><p class="card-price">303.50$</p><span class="card-add"></span></div>
  <div class="card"><span class="badge">NEW</span><div class="card-img meter" role="img" aria-label="Taximeter with red display"></div><p class="card-name">Placeholder product Style</p><p class="card-price">303.50$</p><span class="card-add"></span></div>
</main>

<div class="abs pager-rule"></div>
<div class="abs pager-info">Showing of 1-12 of 125 results</div>
<div class="abs pager">
  <span style="width:36px">PREV</span>
  <span style="width:23px">1</span>
  <span style="width:23px">2</span>
  <span style="width:36px">NEXT</span>
</div>

<footer class="abs footer">
  <div class="f-col" style="left:149px;width:98px">
    <h4>ABOUT <span>FARELANE</span></h4>
    We provide quality dispatch and meter equipment for indecent taxi &amp; fleet vendors.
  </div>
  <div class="f-col" style="left:256px">
    <h4>CONTACT INFO</h4>
    Shop Office: (555) 201-4478<br>
    Customer service: (555) 3301-8812<br>
    Email: <a>hello@farelane.com</a>
  </div>
  <div class="f-col" style="left:362px">
    <h4>HOURS OF SERVICE</h4>
    Monday - Friday: 09:00AM - 09:00PM<br>
    Saturday: 09:00AM - 07:00PM<br>
    Sunday: Closed
  </div>
  <div class="f-col" style="left:468px">
    <h4>LINK <span>US</span></h4>
    <div class="socials"><i></i><i></i><i></i><i></i><i></i></div>
  </div>
  <div class="f-rule"></div>
  <div class="f-copy">© 2018 <span>Farelane.com</span> &nbsp;&nbsp;&nbsp; | &nbsp;Trademarks and brands are the property of their respective owners.</div>
</footer>

</body>
</html>
```